Re-Design of Business Card for Marine Sales People

We are looking to Re-design our business cards to look like they are in the 21st century. We are a full service marina and sell a lot of new/used boats. May want a spot on the card for our 3 main brands we sell. A picture spot of the sales man would be nice, but not necessarily.

```html
<!DOCTYPE html>
<html lang="en">
<head>
<meta charset="utf-8">
<title>Harrowmere Marine – Business Card</title>
<link rel="stylesheet" href="https://fonts.googleapis.com/css2?family=Jost:ital,wght@1,500&family=Poppins:wght@400;600&display=swap">
<style>
  :root {
    --navy: #112d54;
    --sky: #00a0e0;
    --white: #ffffff;
    --backdrop: #ededed;
    --shadow: rgba(0, 0, 0, 0.32);
  }
  * { box-sizing: border-box; margin: 0; padding: 0; }
  html, body {
    width: 1200px; height: 1200px; overflow: hidden;
    background: var(--backdrop);
  }
  .canvas { position: relative; width: 1200px; height: 1200px; }

  .card {
    position: absolute; left: 181px; width: 838px; height: 478px;
    overflow: hidden;
    box-shadow: 24px 24px 14px var(--shadow);
  }
  .card--front { top: 110px; background: var(--navy); }
  .card--back { top: 611px; background: var(--white); }

  /* tagline: plain text, two lines */
  .tagline {
    position: absolute; text-align: center;
    font-family: "Poppins", sans-serif; font-weight: 600; line-height: 1.5;
  }
  .tagline--front { left: 600px; top: 56px; width: 244px; font-size: 18px; color: var(--white); }
  .tagline--back { left: 533px; top: 64px; width: 248px; font-size: 18px; color: var(--navy); }

  /* company name: one colour, one weight, one plain square beside it */
  .company {
    position: absolute; display: flex; align-items: center; justify-content: center;
    font-family: "Poppins", sans-serif; font-weight: 600; line-height: 1; white-space: nowrap;
  }
  .company__mark { flex: none; background: currentColor; }
  .company--front { left: 0; top: 208px; width: 838px; font-size: 44px; gap: 18px; color: var(--white); }
  .company--front .company__mark { width: 30px; height: 30px; }
  .company--back { left: 20px; top: 70px; width: 420px; font-size: 28px; gap: 12px; color: var(--navy); }
  .company--back .company__mark { width: 20px; height: 20px; }

  .location {
    position: absolute; text-align: center; color: var(--navy);
    font-family: "Jost", sans-serif; font-style: italic; font-weight: 500;
  }
  .location-band {
    position: absolute; left: 0; top: 375px; width: 100%; height: 46px;
    background: var(--white);
  }
  .location--front { left: 0; top: 375px; width: 100%; line-height: 46px; font-size: 26px; }
  .location--back { left: 20px; top: 140px; width: 420px; font-size: 17px; }

  /* back card structure */
  .accent-bar { position: absolute; left: 806px; top: 0; width: 32px; height: 221px; background: var(--sky); }
  .avatar-tab {
    position: absolute; left: 756px; top: 221px; width: 82px; height: 70px;
    background: var(--sky); border-radius: 3px 0 0 3px;
    display: flex; align-items: center; justify-content: center;
  }
  .contact-rail {
    position: absolute; left: 0; top: 222px; width: 72px; height: 256px;
    background: var(--navy); border-radius: 0 4px 0 0;
  }
  .footer-strip { position: absolute; left: 404px; top: 453px; width: 434px; height: 25px; }

  .contact-list { list-style: none; }
  .contact {
    position: absolute; left: 0; height: 30px; display: flex; align-items: center;
  }
  .contact__icon { width: 72px; display: flex; justify-content: center; }
  .contact__text {
    margin-left: 15px; padding-bottom: 3px;
    border-bottom: 2px solid var(--sky);
    font-family: "Poppins", sans-serif; font-size: 17px; color: var(--navy);
    white-space: nowrap;
  }
  .contact--email { top: 244px; }
  .contact--web { top: 292px; }
  .contact--phone { top: 340px; }
  .contact--address { top: 390px; }
  .contact--email .contact__text { width: 218px; }
  .contact--web .contact__text { width: 208px; }
  .contact--phone .contact__text { width: 289px; }
  .contact--address .contact__text { width: 224px; }

  .person { position: absolute; left: 500px; top: 224px; font-family: "Poppins", sans-serif; }
  .person__name { font-size: 42px; font-weight: 600; color: var(--navy); line-height: 1.2; }
  .person__role { font-size: 20px; font-weight: 400; color: var(--sky); line-height: 1.3; }
</style>
</head>
<body>
<main class="canvas">

  <section class="card card--front" aria-label="Card front">
    <p class="tagline tagline--front">On the Water<br>Since 1981</p>
    <h1 class="company company--front"><span class="company__mark" aria-hidden="true"></span>HARROWMERE MARINE</h1>
    <div class="location-band"></div>
    <p class="location location--front">Lake Harrowmere, Eastbrook, NH</p>
  </section>

  <section class="card card--back" aria-label="Card back">
    <div class="accent-bar"></div>
    <div class="avatar-tab">
      <svg width="28" height="34" viewBox="0 0 28 34" aria-hidden="true">
        <circle cx="14" cy="9" r="8" fill="var(--white)"/>
        <path d="M0 34 V28 Q0 19 14 19 Q28 19 28 28 V34 Z" fill="var(--white)"/>
      </svg>
    </div>

    <h2 class="company company--back"><span class="company__mark" aria-hidden="true"></span>HARROWMERE MARINE</h2>
    <p class="location location--back">Lake Harrowmere, Eastbrook, NH</p>

    <p class="tagline tagline--back">On the Water<br>Since 1981</p>

    <div class="person">
      <p class="person__name">Your Name</p>
      <p class="person__role">Your Position</p>
    </div>

    <div class="contact-rail"></div>
    <ul class="contact-list">
      <li class="contact contact--email">
        <span class="contact__icon"><svg width="26" height="20" viewBox="0 0 26 20" aria-hidden="true"><rect x="1" y="1" width="24" height="18" rx="2" fill="var(--white)"/><path d="M3 4 L13 12 L23 4 M3 17 L10 10 M23 17 L16 10" fill="none" stroke="var(--navy)" stroke-width="1.6"/></svg></span>
        <span class="contact__text">Youremail@mailhub.com</span>
      </li>
      <li class="contact contact--web">
        <span class="contact__icon"><svg width="26" height="26" viewBox="0 0 26 26" aria-hidden="true"><circle cx="13" cy="13" r="12" fill="var(--white)"/><g fill="none" stroke="var(--navy)" stroke-width="1.6"><ellipse cx="13" cy="13" rx="5" ry="12"/><path d="M1 13 H25 M3 7 H23 M3 19 H23 M13 1 V25"/></g></svg></span>
        <span class="contact__text">www.yourwebsite.com</span>
      </li>
      <li class="contact contact--phone">
        <span class="contact__icon"><svg width="24" height="24" viewBox="0 0 24 24" aria-hidden="true"><path d="M5 2 L9 2 L10 7 L7.5 9 Q9.5 13.5 14 16 L16 13.5 L21 14.5 L21 18.5 Q20 22 16 21.5 Q4 19 2.5 7 Q2.5 3 5 2 Z" fill="var(--white)"/><path d="M14 3 Q20 4 21 10 M14 6.5 Q17.5 7 18 10" fill="none" stroke="var(--white)" stroke-width="1.8"/></svg></span>
        <span class="contact__text">+99999 99999,&nbsp; +88888 88888</span>
      </li>
      <li class="contact contact--address">
        <span class="contact__icon"><svg width="22" height="28" viewBox="0 0 22 28" aria-hidden="true"><path d="M11 27 Q1 16 1 10.5 A10 10 0 0 1 21 10.5 Q21 16 11 27 Z" fill="var(--white)"/><circle cx="11" cy="10.5" r="4" fill="var(--navy)"/></svg></span>
        <span class="contact__text">Your Company Address.</span>
      </li>
    </ul>

    <svg class="footer-strip" viewBox="0 0 434 25" preserveAspectRatio="none" aria-hidden="true"><path d="M0 25 L34 0 H434 V25 Z" fill="var(--navy)"/></svg>
  </section>

</main>
</body>
</html>
```